Time for a better IT consulting company?

We are a mobile computer consulting company, taking care of client's issues remotely or at their site. Website of company www.qr-lumotek.com. Business card is an example of marketing so far.
We moved this year but we still service our existing clients. We have expanded our number of technicians available. We would like to use this card for both new business and reaching out to old business.

Target Market(s)

This should target businesses and referrals to businesses from our existing clients as well as a new client outreach for our new location.

Industry/Entity Type

Computer

Requirements
Must have
• This postcard will let clients know we have moved into or we continue to service their area. Make sure it says Inc, not LLC. Must incorporate existing theme in some fashion.
Nice to have
• Themes to communicate: team of people standing by, stability, faster response time, accessibility.
• Areas of coverage: Westchester, Rockland, Manhattan, The Bronx, lower Connecticut.
Should not have
• Cartoon feel.

```html
<!DOCTYPE html>
<html lang="en">
<head>
<meta charset="utf-8">
<title>Lumotek Computer Consulting – Postcard</title>
<link href="https://fonts.googleapis.com/css2?family=Arimo:ital,wght@0,400;0,700;1,700&display=swap" rel="stylesheet">
<style>
  :root {
    --sky: #38b2e4;
    --blue: #1e7fc6;
    --navy: #0e3150;
    --navy-mid: #1c5678;
    --ink: #333b42;
    --grey: #8a8f94;
    --paper: #ffffff;
    --stage: #e9ebed;
    --strip: #0b0b0b;
  }
  * { box-sizing: border-box; margin: 0; padding: 0; }
  html, body { width: 1200px; height: 1000px; overflow: hidden; }
  body {
    background: var(--stage);
    font-family: "Arimo", Arial, sans-serif;
    color: var(--ink);
    position: relative;
  }
  .card {
    position: absolute;
    width: 570px;
    height: 440px;
    background: var(--paper);
    box-shadow: 0 6px 18px rgba(0,0,0,.18);
    overflow: hidden;
  }
  .card--back { left: 20px; top: 280px; }
  .card--front { left: 610px; top: 280px; }

  /* ---------- back ---------- */
  .services-banner {
    position: absolute; left: 0; top: 30px;
    width: 275px; height: 28px;
    background: linear-gradient(90deg, var(--navy), var(--navy-mid));
    clip-path: polygon(0 0, 100% 0, 94% 100%, 0 100%);
    color: #fff; font-weight: 700; font-size: 15px;
    line-height: 28px; padding-left: 22px;
  }
  .stamp-box {
    position: absolute; right: 22px; top: 22px;
    width: 122px; height: 122px;
    border: 1.5px solid var(--grey);
  }
  .services-list {
    position: absolute; left: 34px; top: 74px;
    list-style: none; font-size: 12.5px; line-height: 17.5px; color: #222;
  }
  .services-list li::before { content: "•"; margin-right: 5px; }
  .services-list li:nth-child(n) { padding-left: calc((var(--i, 0)) * 1px); }
  .tagline {
    position: absolute; left: 58px; top: 250px;
    font-style: italic; font-weight: 700; font-size: 20px; line-height: 22px;
    color: var(--blue);
  }
  .tagline .accent { color: var(--sky); }

  .brand { position: absolute; display: flex; align-items: center; gap: 10px; }
  .brand__dot { border-radius: 50%; background: var(--navy-mid); flex: none; }
  .brand__name { font-weight: 700; color: #4a4f55; line-height: 1.15; }

  .card--back .brand { left: 58px; top: 318px; }
  .card--back .brand__dot { width: 36px; height: 36px; }
  .card--back .brand__name { font-size: 14px; }

  .back-contacts {
    position: absolute; left: 96px; top: 362px; width: 300px;
    font-size: 9px; line-height: 14px; color: #222;
  }
  .back-contacts .row { display: flex; align-items: center; gap: 4px; }
  .back-contacts .coverage-label { color: var(--sky); font-weight: 700; }
  .back-contacts .side { position: absolute; left: 170px; top: 0; }

  .icon { width: 11px; height: 11px; flex: none; fill: var(--sky); }

  /* ---------- front ---------- */
  .headline {
    position: absolute; left: 30px; top: 24px;
    font-weight: 700; font-size: 34px; line-height: 36px;
    color: var(--sky); letter-spacing: -.2px;
  }
  .hero-band {
    position: absolute; left: 0; top: 112px; width: 570px; height: 204px;
    background: linear-gradient(180deg, var(--navy-mid) 0%, var(--navy) 100%);
  }
  .hero-band__frame { position: absolute; inset: 0; }
  .hero-photo {
    position: absolute; left: 0; top: 0; width: 570px; height: 204px;
    background: linear-gradient(135deg, #e6ecef 0%, #c9d3d9 45%, #8e9aa4 100%);
    clip-path: polygon(284px 0, 556px 0, 518px 204px, 238px 204px);
  }
  .hero-copy { position: absolute; left: 30px; top: 20px; width: 230px; color: #fff; }
  .hero-copy__title { font-size: 17px; line-height: 21px; font-weight: 400; }
  .hero-copy__title .accent { color: var(--sky); display: block; }
  .hero-copy__rule { height: 1px; background: rgba(255,255,255,.8); margin: 8px 0 8px; width: 222px; }
  .hero-list { list-style: none; font-size: 11.5px; line-height: 19.6px; }
  .hero-list li { display: flex; align-items: center; gap: 8px; }
  .hero-list li::before {
    content: ""; width: 0; height: 0;
    border-left: 7px solid var(--sky);
    border-top: 4.5px solid transparent; border-bottom: 4.5px solid transparent;
  }
  .promise-strip {
    position: absolute; left: 0; top: 316px; width: 570px; height: 21px;
    background: var(--strip); color: #fff;
    font-size: 10.5px; line-height: 21px; text-align: center;
  }
  .promise-strip strong { font-weight: 700; }
  .card--front .brand { left: 48px; top: 360px; }
  .card--front .brand__dot { width: 44px; height: 44px; }
  .card--front .brand__name { font-size: 18px; }
  .front-contacts {
    position: absolute; left: 370px; top: 354px;
    font-size: 11px; line-height: 17px; color: #222;
  }
  .front-contacts .row { display: flex; align-items: center; gap: 8px; }
</style>
</head>
<body>

<section class="card card--back" aria-label="Postcard back">
  <div class="services-banner">We have also Expand our Services</div>
  <div class="stamp-box" aria-hidden="true"></div>
  <ul class="services-list">
    <li>It Staffing</li>
    <li>PC &amp; MAC</li>
    <li>Home &amp; Office</li>
    <li>Website and Wiring</li>
    <li>Wireless and Cellur Solutions</li>
    <li>New Equipment Purchase &amp; Upgrades</li>
    <li>Hardware, Software &amp; Security Consulting</li>
    <li>Server and Syaytem Monitoring &amp; Maintenance</li>
    <li>Remote Online Assistance with Computer Issues</li>
  </ul>
  <p class="tagline">Our technicians <span class="accent">are ready</span><br>to solve your problems.</p>
  <div class="brand">
    <span class="brand__dot" aria-hidden="true"></span>
    <span class="brand__name">Lumotek Computer<br>Consulting, Inc.</span>
  </div>
  <div class="back-contacts">
    <div class="row"><svg class="icon" viewBox="0 0 12 12"><path d="M6 1 1 5.5h1.5V11h3V8h1v3h3V5.5H11z"/></svg>Lumotek Computer Consulting</div>
    <div class="row"><svg class="icon" viewBox="0 0 12 12"><path d="M1 3h10v6H1z M1 3l5 3.5L11 3"/></svg>info@qr-lumotek.com</div>
    <div><span class="coverage-label">Areas of coverage :</span> Westchester, Rockland, Manhattan,<br>The Bronx, lower Connecticut.</div>
    <div class="side">
      <div class="row"><svg class="icon" viewBox="0 0 12 12"><path d="M3.5 1h5v10h-5z M4.5 2v7h3V2z"/></svg>555-014-2290</div>
      <div class="row"><svg class="icon" viewBox="0 0 12 12"><circle cx="6" cy="6" r="5"/></svg>www.qr-lumotek.com</div>
    </div>
  </div>
</section>

<section class="card card--front" aria-label="Postcard front">
  <h1 class="headline">Need immediate assistance<br>with a computer issue?</h1>
  <div class="hero-band">
    <svg class="hero-band__frame" width="570" height="204" viewBox="0 0 570 204" aria-hidden="true">
      <polygon points="277,0 286,0 240,204 231,204" fill="var(--sky)"/>
      <polygon points="556,0 563,0 525,204 518,204" fill="var(--sky)"/>
    </svg>
    <div class="hero-photo" role="img" aria-label="Photo of a smiling team of IT consultants helping a client at an office computer"></div>
    <div class="hero-copy">
      <h2 class="hero-copy__title">Get Help from Professional <span class="accent">IT Service Experts</span></h2>
      <div class="hero-copy__rule"></div>
      <ul class="hero-list">
        <li>Home &amp; office support</li>
        <li>Full-time network monitoring</li>
        <li>Data backup and security</li>
        <li>Wireless and Cellular solutions</li>
        <li>Personal on-site visits</li>
        <li>Online remote computer support</li>
      </ul>
    </div>
  </div>
  <p class="promise-strip">Fast and Reliable <strong>Online computer consulting company</strong> for better and more cost effective solutions</p>
  <div class="brand">
    <span class="brand__dot" aria-hidden="true"></span>
    <span class="brand__name">Lumotek Computer<br>Consulting, Inc.</span>
  </div>
  <div class="front-contacts">
    <div class="row"><svg class="icon" viewBox="0 0 12 12"><path d="M6 1 1 5.5h1.5V11h3V8h1v3h3V5.5H11z"/></svg>Lumotek Computer Consulting</div>
    <div class="row"><svg class="icon" viewBox="0 0 12 12"><path d="M3.5 1h5v10h-5z M4.5 2v7h3V2z" fill-rule="evenodd"/></svg>555-014-2290</div>
    <div class="row"><svg class="icon" viewBox="0 0 12 12"><path d="M1 3h10v6H1z"/></svg>info@qr-lumotek.com</div>
    <div class="row"><svg class="icon" viewBox="0 0 12 12"><circle cx="6" cy="6" r="5"/></svg>www.qr-lumotek.com</div>
  </div>
</section>

</body>
</html>
```